Web re-design project for web software development agency

We need to re-design our existing website (www.tremondesign.co.uk), and are going to start using a shorter domain (www.tremon.com).
We have been in business for 8 years and it's time for an update.

We are based at Harrowmere Lodge (home of the code breakers). We specialise in writing software for the web. Over the years we have built up a healthy customer base and it is time to incorporate the features we build for our customers into our own site (e.g. social media).

We have a team of 8 talented developers with varied skills including: apps for mobile; complex server side software; front-end software; eCommerce software; specialised web based applications; integration software; hardware support; consultancy services. Our customers are diverse (e.g. banking; commerce; veterinary; R&D; health sector; law; accounting; film industry etc.).

Our current colour scheme is blue, white and green although we are not averse to moving away from these colours. We will also be dropping the DESIGN from our name and logo. Revised logo will be attached.

The site needs to be modern, sophisticated and leading edge. We want to show visitors to the site that we are a professional organisation.
Updates

Our logo in PSD format has been uploaded. Please drop the word DESIGN from the logo.

The deliverable for this project is a PSD (ideally we would like to see how the home page, portfolio page, resources page with mugshots, and forms are going to look).

Many thanks,
Tom

Please DO NOT include a Careers section 

We will also need a "meet our team" section with spaces for 10 photographs as well as some space underneath them so that we can add a short paragraph for each one of them.

Target Market(s)

Mainly large corporations needing bespoke web software, or generally complex projects (for anyone).

Industry/Entity Type

Software

Requirements
Must have
• We would like a home page designed that has the following elements on it:
- Show the new cookie compliance policy displayed probably in the top of the page (will disappear).
- A client Testimonial.
- Pricing icon.
- Social media Links.
- A Quote section in expand/collapse field as in (http://www.quorvix-online.co.uk/our-services.shtml)

We would also like a portfolio page that showcases our clients in an interesting way.

Finally, we would like a form design that we can use throughout the site (i.e. how should buttons, radio buttons, checkboxes, dropdowns, text areas etc. look)?
Nice to have
• A page that follows these guidelines:
http://www.pagelumo.com/the-anatomy-of-a-perfect-landing-page

Here are a few examples of sites in our sector that we like:
- http://www.mellow-craftwork.com/
- http://fendlix.co.uk/
- http://www.wexumo.com/services/web-development (nice contact us page)
- http://www.quorvix-online.co.uk/
- http://www.tasko.com/
- http://www.nethubro.co.uk/
Should not have
• No flash elemets. If anything, we will use html5.

```html
<!DOCTYPE html>
<html lang="en">
<head>
<meta charset="utf-8">
<title>Tremon – Web Application Development and Support</title>
<link href="https://fonts.googleapis.com/css2?family=Arimo:ital,wght@0,400;0,700;1,400;1,700&family=PT+Sans+Narrow:wght@400;700&family=Questrial&family=Noto+Serif:ital@1&display=swap" rel="stylesheet">
<style>
:root{
  --teal:#2f7f8c;
  --teal-tile:#4c98a8;
  --lime:#b4c835;
  --navy:#1f3a6a;
  --ink:#333;
  --muted:#999;
  --bg:#e3e6e8;
  --line:#c9cdd0;
  --white:#fff;
  --link:#2a45a5;
}
*{box-sizing:border-box;margin:0;padding:0}
html,body{width:935px;height:1200px;overflow:hidden}
body{position:relative;background:var(--white);font-family:Arimo,Arial,sans-serif;color:var(--ink)}
.stage{position:absolute;left:0;top:0;width:935px;height:946px;background:radial-gradient(ellipse at 50% 40%,#f2f3f4 0%,var(--bg) 75%)}
.abs{position:absolute}

/* navigation */
.nav{left:99px;top:12px;height:22px;display:flex;align-items:center;font-size:12px;color:#666;white-space:nowrap}
.nav .home{background:var(--teal);color:#fff;font-weight:700;padding:0 8px;height:22px;display:flex;align-items:center;gap:12px;border-radius:2px;margin-right:16px}
.nav .home svg{width:8px;height:5px}
.nav a{color:#666;text-decoration:none}
.nav .sep{color:#bbb;margin:0 6px}
.search{left:642px;top:11px;width:192px;height:24px;border:1px solid #ccc;border-radius:12px;background:#fff;font-size:11px;font-style:italic;color:#aaa;padding:5px 12px}
.search svg{position:absolute;right:9px;top:5px;width:13px;height:13px}

/* brand */
.logo{left:104px;top:53px}
.logo .mark{width:34px;height:34px;background:var(--lime);display:block;margin-bottom:2px}
.logo .name{font-family:Questrial,sans-serif;font-size:30px;color:var(--white);letter-spacing:-.5px;line-height:1;text-shadow:0 0 1px #999}
.tagline{left:482px;top:104px;width:348px;text-align:right;font-size:14px;font-weight:700;color:var(--teal);letter-spacing:-.4px}

/* mosaic */
.tile{position:absolute}
.tile.photo-blue{background:linear-gradient(135deg,#1b3c82,#3c6cc4)}
.tile.photo-office{background:linear-gradient(135deg,#c9d5e2,#8faac4)}
.tile.photo-person{background:linear-gradient(160deg,#e9e6e2,#b9b4ae)}
.tile.text{background:var(--teal-tile);color:#eef6f8;font-family:"PT Sans Narrow",sans-serif;font-size:13.5px;line-height:18px;padding:10px 7px}
.tile.text.just{text-align:justify}
.label{position:absolute;font-family:"PT Sans Narrow",sans-serif;font-weight:700;font-size:16px;padding:3px 14px;line-height:18px}
.label.light{background:#eaeef1;color:#222}
.label.lime{background:var(--lime);color:#fff}
.label.navy{background:var(--navy);color:#fff}
.arrow{position:absolute;width:34px;height:34px;border-radius:50%;background:#f5f6f7;border:1px solid #d6d9db}
.arrow svg{position:absolute;left:11px;top:9px;width:12px;height:16px}

/* featured services */
.featured{left:82px;top:481px;width:387px;height:420px;border:1px solid #c2c6c9;background:linear-gradient(180deg,#e6e8ea,#dcdfe1);padding:24px 16px 0 17px}
.featured h2{font-weight:400;font-size:21px;color:var(--teal);margin-bottom:18px}
.featured p{font-size:11px;line-height:16px;margin-bottom:15px;letter-spacing:-.1px}
.featured p a{display:block;text-align:right;color:var(--link);text-decoration:none;line-height:16px;margin-top:-16px}

/* accordions */
.acc-head{position:absolute;left:505px;width:230px;background:var(--teal);color:#fff;font-size:20px;padding:4px 31px}
.acc-panel{position:absolute;left:505px;width:359px;border:1px solid #d3d6d9;background:rgba(230,232,234,.6)}
.acc-row{position:absolute;left:13px;width:334px;border-bottom:1px solid var(--line)}
.acc-row .t{position:absolute;left:5px;bottom:10px;font-style:italic;font-weight:700;font-size:15px;color:#8a8a8a}
.acc-row .m{position:absolute;right:36px;bottom:6px;font-size:10.5px;color:var(--muted);letter-spacing:.2px}
.acc-row svg{position:absolute;right:6px;bottom:8px;width:15px;height:9px}

/* footer */
.legal{left:60px;top:988px;width:126px;text-align:right;font-family:"Noto Serif",serif;font-style:italic;font-size:10.5px;color:#888;line-height:17px}
.social{left:118px;top:1098px;display:flex;gap:6px;font-size:9px;color:#888}
.social span{display:flex;align-items:center;gap:2px}
.social i{display:inline-block;width:8px;height:8px;background:#5b8fc7}
.social span:last-child i{background:#e98a2d}
.ftitle{font-size:11px;color:#555;letter-spacing:.2px}
.testimonials{left:298px;top:991px;width:238px}
.testimonials .item{border-bottom:1px solid #e2e2e2;padding:22px 0 12px 0}
.testimonials .item + .item{padding-top:14px}
.testimonials h4{font-size:12px;font-weight:700;color:#222}
.testimonials .meta{font-family:"Noto Serif",serif;font-style:italic;font-size:10px;color:#888;margin-top:12px}
.clients{left:596px;top:991px}
.client{position:absolute;display:flex;align-items:center;justify-content:center;gap:4px;font-size:10px;font-weight:700;color:#555;border:1px solid #ccc;background:#fafafa;padding:0 4px;white-space:nowrap}
.client b{display:inline-block;width:7px;height:7px;background:#c2c7cc}
</style>
</head>
<body>
<div class="stage"></div>

<nav class="nav abs">
  <span class="home">HOME <svg viewBox="0 0 8 5"><path d="M0 0h8L4 5z" fill="#fff"/></svg></span>
  <a href="#">ABOUT US</a><span class="sep">|</span>
  <a href="#">SERVICES</a><span class="sep">|</span>
  <a href="#">TECHNOLOGY</a><span class="sep">|</span>
  <a href="#">PORTFOLIO</a><span class="sep">|</span>
  <a href="#">CONTACT US</a>
</nav>
<div class="search abs">Search line
  <svg viewBox="0 0 13 13"><circle cx="5" cy="5" r="4" fill="none" stroke="#999" stroke-width="1.6"/><path d="M8 8l4 4" stroke="#999" stroke-width="2"/></svg>
</div>

<div class="logo abs"><span class="mark"></span><div class="name">TREMON</div></div>
<div class="tagline abs">WEB APPLICATION DEVELOPMENT AND SUPPORT</div>

<section class="mosaic">
  <div class="tile photo-person" style="left:105px;top:139px;width:58px;height:60px" role="img" aria-label="Hand signing a document"></div>
  <div class="tile photo-person" style="left:105px;top:200px;width:58px;height:59px" role="img" aria-label="Portrait of a team member"></div>
  <div class="tile photo-person" style="left:105px;top:261px;width:58px;height:119px" role="img" aria-label="Portrait of a team member holding a folder"></div>
  <div class="tile photo-blue" style="left:105px;top:382px;width:58px;height:60px" role="img" aria-label="Computer screen in blue light"></div>

  <div class="tile photo-blue" style="left:166px;top:139px;width:180px;height:182px;background:linear-gradient(160deg,#0d1f4d,#2d63b8 60%,#0a1a40)" role="img" aria-label="Globe with network connections"></div>
  <div class="label light" style="left:173px;top:280px;width:154px">WHO WE ARE?</div>

  <div class="tile text just" style="left:348px;top:139px;width:119px;height:182px">Lorem ipsum dolor sit amet, consectetur adipisicing elit, sed do eiusmod tempor incididunt ut labore et dolore magna aliqua. Ut enim ad minim veniam, quis nostrud exercitation laborum.</div>

  <div class="tile photo-office" style="left:469px;top:139px;width:242px;height:181px" role="img" aria-label="Developer working at a keyboard with charts"></div>
  <div class="label lime" style="left:469px;top:281px;width:161px">OUR PASSION...</div>

  <div class="tile text" style="left:712px;top:139px;width:120px;height:181px;padding-top:31px">Our passion is developing complex applications for the web that work for you and your business.</div>

  <div class="tile photo-office" style="left:166px;top:324px;width:241px;height:118px;background:linear-gradient(135deg,#d8dde3,#9fb0c2)" role="img" aria-label="Team of colleagues in an office"></div>
  <div class="label navy" style="left:166px;top:411px;width:161px">OUR WORK...</div>

  <div class="tile text" style="left:409px;top:324px;width:241px;height:118px;padding:29px 10px">Lorem ipsum dolor sit amet, consectetur adipisicing elit, sed do eiusmod tempor incididunt ut labore et dolore magna aliqua.</div>

  <div class="tile photo-blue" style="left:652px;top:324px;width:58px;height:118px" role="img" aria-label="Computer screen in blue light"></div>
  <div class="tile photo-office" style="left:712px;top:324px;width:120px;height:118px;background:linear-gradient(135deg,#e4e7ea,#a7b2bd)" role="img" aria-label="Two business people shaking hands"></div>

  <div class="arrow" style="left:72px;top:394px"><svg viewBox="0 0 12 16"><path d="M9 1L3 8l6 7" fill="none" stroke="#2f7f8c" stroke-width="2"/></svg></div>
  <div class="arrow" style="left:829px;top:394px"><svg viewBox="0 0 12 16"><path d="M3 1l6 7-6 7" fill="none" stroke="#2f7f8c" stroke-width="2"/></svg></div>
</section>

<section class="featured abs">
  <h2>Featured Services</h2>
  <p>Lorem ipsum dolor sit amet, consectetur adipisicing elit, sed do eiusmod tempor incididunt ut labore et dolore magna aliqua. Ut enim ad minim veniam.<a href="#">more++</a></p>
  <p>Lorem ipsum dolor sit amet, consectetur adipisicing elit, sed do eiusmod tempor incididunt ut labore et dolore magna aliqua. Ut enim ad minim veniam.<a href="#">more++</a></p>
  <p>Lorem ipsum dolor sit amet, consectetur adipisicing elit, sed do eiusmod tempor incididunt ut labore et dolore magna aliqua. Ut enim ad minim veniam.<a href="#">more++</a></p>
  <p>Lorem ipsum dolor sit amet, consectetur adipisicing elit, sed do eiusmod tempor incididunt ut labore et dolore magna aliqua. Ut enim ad minim veniam.<a href="#">more++</a></p>
  <p>Lorem ipsum dolor sit amet, consectetur adipisicing elit, sed do eiusmod tempor incididunt ut labore et dolore magna aliqua. Ut enim ad minim veniam.<a href="#">more++</a></p>
</section>

<svg width="0" height="0" style="position:absolute"><defs><symbol id="chev" viewBox="0 0 15 9"><path d="M1 1l6.5 6.5L14 1" fill="none" stroke="#2f7f8c" stroke-width="2"/></symbol></defs></svg>

<div class="acc-head" style="top:478px;height:31px">Our Work</div>
<div class="acc-panel" style="top:509px;height:176px">
  <div class="acc-row" style="top:0;height:41px"><span class="t">Work Topic</span><span class="m">SHOW MORE</span><svg><use href="#chev"/></svg></div>
  <div class="acc-row" style="top:41px;height:45px"><span class="t">Work Topic</span><span class="m">SHOW MORE</span><svg><use href="#chev"/></svg></div>
  <div class="acc-row" style="top:86px;height:40px"><span class="t">Work Topic</span><span class="m">SHOW MORE</span><svg><use href="#chev"/></svg></div>
  <div class="acc-row" style="top:126px;height:39px"><span class="t">Work Topic</span><span class="m">SHOW MORE</span><svg><use href="#chev"/></svg></div>
</div>

<div class="acc-head" style="top:700px;height:30px;padding-top:3px">Our Technology</div>
<div class="acc-panel" style="top:731px;height:177px">
  <div class="acc-row" style="top:0;height:39px"><span class="t">Service</span><span class="m">SHOW MORE</span><svg><use href="#chev"/></svg></div>
  <div class="acc-row" style="top:39px;height:39px"><span class="t">Service</span><span class="m">SHOW MORE</span><svg><use href="#chev"/></svg></div>
  <div class="acc-row" style="top:78px;height:39px"><span class="t">Service</span><span class="m">SHOW MORE</span><svg><use href="#chev"/></svg></div>
  <div class="acc-row" style="top:117px;height:39px"><span class="t">Service</span><span class="m">SHOW MORE</span><svg><use href="#chev"/></svg></div>
</div>

<footer>
  <div class="legal abs">Copyright Statement<br>Terms &amp; Conditions<br>Privacy Policy</div>
  <div class="social abs"><span><i></i>Chirpline</span><span><i></i>Circlet</span><span><i></i>Feed</span></div>

  <div class="testimonials abs">
    <div class="ftitle">TESTIMONIALS</div>
    <div class="item"><h4>I create new design!</h4><div class="meta">Date, Time &nbsp;&nbsp;•&nbsp;&nbsp; 12 comments</div></div>
    <div class="item"><h4>I create new design!</h4><div class="meta">Date, Time &nbsp;&nbsp;•&nbsp;&nbsp; 12 comments</div></div>
  </div>

  <div class="clients abs">
    <div class="ftitle">OUR CLIENTS</div>
    <div class="client" style="left:0;top:22px;width:92px;height:27px"><b></b>AurumVault</div>
    <div class="client" style="left:121px;top:19px;width:58px;height:44px">Lumiveon</div>
    <div class="client" style="left:0;top:79px;width:100px;height:24px"><b></b>Rattlebox Records</div>
    <div class="client" style="left:106px;top:79px;width:88px;height:22px"><b></b>Veltrana</div>
  </div>
</footer>
</body>
</html>
```